Dance Card to Provide Contact Info

I'm looking for a double sided business card to provide contact information to perspective dance partners.
One side of the card would have the words: "Yes I would love to Dance" written in an interesting and eye catching way. Below that would be the three categories I'm interested in
>Social >Exhibition >Competition
The other side of the card would include a picture of me with my Name, Phone Number, and Email Address (Dale Penwick, 210-547-2183, dale@twirlmerry.dance)
My target market is middle aged women interested in Country and Western dancing and West Coast Swing dancing. I am NOT particularly interested in Ballroom style.
Here are a few links to the type of dancing I want to do:
http://www.fpqlx.org/
http://www.prairiestepguildnetwork.com/
http://bexarridgepartnerspin.com/
Business
Contact Information for Business Card
Dale Penwick
210-547-2183
dale@twirlmerry.dance

```html
<!DOCTYPE html>
<html lang="en">
<head>
<meta charset="utf-8">
<title>Dale Penwick – Dance Card</title>
<link rel="stylesheet" href="https://fonts.googleapis.com/css2?family=Pinyon+Script&family=Source+Sans+3:wght@400&display=swap">
<style>
  :root {
    --ink-navy: #1f2a36;
    --paper-white: #ffffff;
    --page-bg: #eceae7;
    --text-dark: #1b1b1b;
    --portrait-top: #c98a6a;
    --portrait-bottom: #1a2430;
  }
  html, body {
    margin: 0;
    padding: 0;
    width: 1200px;
    height: 900px;
    overflow: hidden;
    background: var(--page-bg);
  }
  .canvas {
    position: relative;
    width: 1200px;
    height: 900px;
  }
  .card {
    position: absolute;
    width: 556px;
    height: 342px;
    background: var(--ink-navy);
    overflow: hidden;
    box-shadow: 0 4px 14px rgba(0,0,0,0.18);
  }
  .card-front { left: 238px; top: 62px; }
  .card-back { left: 460px; top: 519px; }

  .contact-band {
    position: absolute;
    left: 0;
    top: 224px;
    width: 100%;
    height: 118px;
    background: var(--paper-white);
  }
  .portrait {
    position: absolute;
    left: 0;
    top: 30px;
    width: 256px;
    height: 312px;
    border-radius: 120px 120px 0 0;
    background: linear-gradient(180deg, var(--portrait-top) 0%, var(--portrait-top) 45%, var(--portrait-bottom) 62%, var(--portrait-bottom) 100%);
  }
  .owner-name {
    position: absolute;
    right: 42px;
    top: 100px;
    margin: 0;
    font-family: "Pinyon Script", cursive;
    font-weight: 400;
    font-size: 58px;
    line-height: 1;
    color: var(--paper-white);
  }
  .contact-list {
    position: absolute;
    right: 34px;
    top: 254px;
    margin: 0;
    padding: 0;
    list-style: none;
    font-family: "Source Sans 3", sans-serif;
    font-size: 17px;
    color: var(--text-dark);
    text-align: right;
  }
  .contact-list li {
    display: flex;
    justify-content: flex-end;
    align-items: center;
    gap: 7px;
    height: 25px;
  }
  .contact-list svg { width: 13px; height: 13px; fill: var(--text-dark); }

  .tagline {
    position: absolute;
    left: 0;
    top: 70px;
    width: 100%;
    margin: 0;
    text-align: center;
    font-family: "Pinyon Script", cursive;
    font-weight: 400;
    font-size: 58px;
    line-height: 72px;
    color: var(--paper-white);
  }
  .dance-styles {
    position: absolute;
    left: 0;
    top: 258px;
    width: 100%;
    margin: 0;
    padding: 0;
    list-style: none;
    display: flex;
    justify-content: center;
    gap: 14px;
    font-family: "Source Sans 3", sans-serif;
    font-size: 21px;
    color: var(--paper-white);
  }
  .dance-styles li::before {
    content: "";
    display: inline-block;
    width: 10px;
    height: 10px;
    margin-right: 5px;
    border-radius: 50%;
    background: var(--paper-white);
    vertical-align: 2px;
  }
</style>
</head>
<body>
<main class="canvas">
  <section class="card card-front">
    <div class="contact-band"></div>
    <div class="portrait" role="img" aria-label="Portrait photo of Dale Penwick in a dark shirt"></div>
    <h1 class="owner-name">Dale Penwick</h1>
    <ul class="contact-list">
      <li>210-547-2183
        <svg viewBox="0 0 24 24" aria-hidden="true"><path d="M6.6 10.8a15.1 15.1 0 0 0 6.6 6.6l2.2-2.2c.3-.3.7-.4 1-.2 1.1.4 2.3.6 3.6.6.6 0 1 .4 1 1V20c0 .6-.4 1-1 1A17 17 0 0 1 3 4c0-.6.4-1 1-1h3.5c.6 0 1 .4 1 1 0 1.3.2 2.5.6 3.6.1.3 0 .7-.2 1z"/></svg>
      </li>
      <li>dale@twirlmerry.dance
        <svg viewBox="0 0 24 24" aria-hidden="true"><path d="M2 5h20v14H2z M4 7v1l8 5 8-5V7l-8 5z" fill-rule="evenodd"/></svg>
      </li>
    </ul>
  </section>

  <section class="card card-back">
    <p class="tagline">Yes I would<br>love to Dance</p>
    <ul class="dance-styles">
      <li>Social</li>
      <li>Exhibition</li>
      <li>Competition</li>
    </ul>
  </section>
</main>
</body>
</html>
```